UK Based Internet hosting Company wants a vibrant eCommerce site designed.

We have only just had our logo and brand designed by Pixel Harbor which went so well that we would like to open up our website design project on here too.

The company is called 'Our Server Lantern' and we provide a range of website hosting, dedicated server, domain name and email solutions that people will be able to purchase online in neatly packaged options from the outset.

Our logo and brand is bright turquoise, black & white (samples of branding will be attached with this project) but we would like the website to be very vibrant with good use of white space rather than a black website.

We want to appeal to end users so web designers, developers and people who would like to host their website. But we also want to appeal to resellers that would like to resell our hosting packages too.

We want a big push on social media and blogging on the site as we would like our brand to be 100% up with Chatterly, Quipster, workRing, Vidoplex and Orbitly+. It would be great to have this integrated into the site with share buttons and rating buttons etc.

We would like to see a homepage initially with a view to providing several page layers down to help our in-house developers hook in our back-end into this front end effectively.

Great customer experience and an easy to navigate journey to the checkout when purchasing the hosting packages is paramount !!

We like how the following sites are set-out and presented:

www.plumwebnode.uk
http://www.tagvault.co.uk
https://www.zq7.net/web-hosting/

Target Market(s)

We have 3 target markets.

Target market 1 - end users, consumers such as Web Designers, Developers and small businesses.

Target Market 2 - Resellers, small businesses that would like to resell our services.

Target Market 3 - Medium to large businesses that would like more of a bespoke solution.

Industry/Entity Type

Internet

Requirements
Must have
• Colourful, bright, bold, easy to navigate and to purchase packages.
• Plenty of call to actions, social media, ratings.
• Video case studies and testimonials would be nice.

```html
<!DOCTYPE html>
<html lang="en">
<head>
<meta charset="utf-8">
<title>Our Server Lantern — Home</title>
<link href="https://fonts.googleapis.com/css2?family=Ubuntu:wght@300;400;500;700&family=Open+Sans:ital,wght@0,400;0,600;1,400&display=swap" rel="stylesheet">
<style>
:root{
  --ink:#1b2130;
  --ink-2:#2a3142;
  --teal:#2cb7ae;
  --teal-dark:#1f9a93;
  --teal-light:#5fcfb0;
  --mint:#6cc59a;
  --sky:#6ccbf2;
  --grey-text:#8a8f98;
  --grey-light:#b4b8bf;
  --body:#444a55;
  --line:#e4e6ea;
  --footer:#333436;
  --footer-line:#4a4b4e;
  --white:#ffffff;
  --star:#f5b41e;
}
*{box-sizing:border-box;margin:0;padding:0}
html,body{width:1200px;height:2651px;overflow:hidden}
body{font-family:"Open Sans",Arial,sans-serif;color:var(--body);background:var(--white);position:relative}
.page{position:relative;width:1200px;height:2651px}
section,header,nav,footer{position:absolute;left:0;width:1200px}
.abs{position:absolute}

/* Header */
.topbar{top:0;height:97px;background:var(--ink)}
.brand{left:100px;top:19px;display:flex;align-items:center;gap:12px;color:var(--white);font-family:"Ubuntu",sans-serif}
.brand-mark{width:58px;height:58px;border-radius:50%;background:var(--teal)}
.brand-name{font-size:20px;line-height:23px;font-weight:400}
.social-top{left:470px;top:38px;display:flex;gap:12px;font-family:"Ubuntu",sans-serif;font-size:11px;color:#c9ced8}
.btn-top{top:30px;height:37px;border-radius:3px;background:#3a4254;color:#d8dce4;font-size:12px;display:flex;align-items:center;gap:7px;padding:0 12px}
.btn-login{left:693px;width:76px}
.btn-register{left:779px;width:89px}
.search{left:878px;top:30px;width:222px;height:37px;border-radius:3px;background:#3f4659;color:#9aa1b1;font-size:11px;padding:0 12px;display:flex;align-items:center;justify-content:space-between}

/* Nav */
.mainnav{top:97px;height:46px;background:linear-gradient(90deg,#23ada6,#3fc1b3 60%,#55c8b0)}
.mainnav ul{list-style:none;display:flex;position:absolute;left:99px;top:0;height:46px}
.mainnav li{height:46px;line-height:46px;padding:0 20px;color:var(--white);font-family:"Ubuntu",sans-serif;font-size:12.5px;text-transform:uppercase;letter-spacing:.2px}
.mainnav li.active{background:#1e958f}

/* Hero */
.hero{top:143px;height:414px;background:linear-gradient(100deg,#ffffff 0%,#eef5f6 30%,#dbe9ec 55%,#c9dfe3 100%)}
.hero-visual{left:620px;top:0;width:580px;height:414px;background:radial-gradient(ellipse at 55% 40%,#9ab0b8 0%,#b8ccd2 35%,rgba(210,226,230,0) 75%)}
.hero-title{left:118px;top:140px;font-family:"Ubuntu",sans-serif;font-size:30px;line-height:35px;color:#2b2f36;font-weight:400}
.domain-form{left:118px;top:219px;display:flex;gap:5px}
.domain-input{width:227px;height:43px;background:var(--white);border-radius:3px;box-shadow:0 1px 3px rgba(0,0,0,.12);font-size:11px;color:var(--grey-light);padding:0 14px;display:flex;align-items:center}
.domain-select{width:104px;height:43px;background:var(--white);border-radius:3px;box-shadow:0 1px 3px rgba(0,0,0,.12);font-size:11px;color:var(--grey-text);padding:0 14px;display:flex;align-items:center;justify-content:space-between}
.domain-go{width:40px;height:43px;margin-left:2px;background:var(--teal-dark);border-radius:3px;display:flex;align-items:center;justify-content:center}
.hero-arrow{top:193px}

/* Services */
.services{top:557px;height:314px}
.service{top:69px;width:240px;text-align:center}
.service-icon{width:95px;height:95px;border-radius:50%;margin:0 auto;display:flex;align-items:center;justify-content:center;background:linear-gradient(180deg,#38c1b3,#25a9a4)}
.service-icon.outline{background:var(--white);border:3px solid var(--teal)}
.service h3{font-family:"Ubuntu",sans-serif;font-weight:400;font-size:21px;color:#3a3f47;margin-top:19px}
.service.current h3{color:var(--teal)}
.service p{font-size:11.5px;line-height:19px;color:var(--grey-text);margin-top:6px}
.divider{left:100px;top:313px;width:1000px;height:1px;background:var(--line)}

/* Case studies */
.cases{top:871px;height:369px}
.section-title{width:1200px;text-align:center;font-family:"Ubuntu",sans-serif;font-weight:300;font-size:37px;color:#7d828a}
.cases .section-title{top:67px}
.case{top:124px;height:238px}
.case-1{left:0;width:385px;background:linear-gradient(135deg,#3a3a3a,#1e1e1e 60%,#555)}
.case-2{left:392px;width:414px;background:linear-gradient(135deg,#4a5560,#7a8a99 45%,#34384a)}
.case-3{left:813px;width:387px;background:linear-gradient(135deg,#5a5a5a,#9a9a9a 50%,#6a6a6a)}
.play{position:absolute;left:50%;top:50%;width:38px;height:38px;margin:-19px 0 0 -19px;border-radius:50%;background:rgba(255,255,255,.85);display:flex;align-items:center;justify-content:center}
.play.teal{background:var(--teal)}
.case-arrow{top:221px;width:22px;height:34px;background:rgba(20,20,20,.75);display:flex;align-items:center;justify-content:center}

/* Testimonials */
.testimonials{top:1240px;height:375px;background:linear-gradient(160deg,#22b3b5 0%,#2cbab1 55%,#72cd9e 100%)}
.testimonials .section-title{top:30px;color:var(--white);font-weight:400}
.quote-card{left:212px;top:101px;width:797px;height:198px;background:var(--white);display:flex}
.quote-photo{width:175px;height:198px;background:linear-gradient(180deg,#b9bcbf,#8a8e93)}
.quote-body{padding:26px 30px 0 29px;width:622px}
.quote-name{font-size:12.5px;font-weight:600;color:#333;display:flex;align-items:center;gap:8px}
.quote-name span{font-weight:400;color:#666}
.quote-text{margin-top:20px;font-style:italic;font-size:11.5px;line-height:26px;color:#6a6f77;position:relative;padding-left:36px}
.quote-text .qm{position:absolute;font-family:Georgia,serif;font-style:normal;font-size:44px;color:#555;line-height:1}
.dots{left:0;top:330px;width:1200px;display:flex;justify-content:center;gap:5px}
.dots i{width:10px;height:10px;border-radius:50%;background:#3aa6a2;border:1px solid #2b8f8b}
.dots i.on{background:#3b4a52}

/* Why us */
.why{top:1615px;height:562px}
.why .section-title{top:68px}
.why-intro{left:173px;top:132px;width:855px;text-align:center;font-size:11.5px;line-height:23px;color:var(--grey-light)}
.feature{top:236px;width:290px}
.feature h4{font-family:"Ubuntu",sans-serif;font-weight:400;font-size:16px;color:#3a3f47;display:flex;align-items:center;gap:10px}
.feature p{margin-top:10px;padding-left:31px;font-size:11px;line-height:19px;color:var(--grey-text)}
.vline{top:226px;width:1px;height:105px;background:var(--line)}
.why-line{left:134px;top:359px;width:926px;height:1px;background:var(--line)}
.rating-label{left:0;top:396px;width:1200px;text-align:center;font-family:"Ubuntu",sans-serif;font-size:16px;color:#3a3f47}
.rating-btn{left:458px;top:422px;width:281px;height:59px;background:var(--mint);border-radius:2px;display:flex;align-items:center;justify-content:center;gap:10px;color:var(--white);font-size:12px}

/* Social feed band */
.feed{top:2177px;height:161px;background:var(--sky)}
.feed-badge{left:170px;top:45px;width:69px;height:69px;border-radius:50%;border:2px solid var(--white);display:flex;align-items:center;justify-content:center}
.feed-handle{left:260px;top:44px;font-size:13px;color:var(--white)}
.feed-text{left:260px;top:64px;font-size:17px;font-weight:600;color:var(--white)}
.feed-actions{left:260px;top:100px;display:flex;gap:22px}

/* Footer */
.site-footer{top:2338px;height:313px;background:var(--footer);color:#d7d8da}
.contact-strip{left:0;top:26px;width:1200px;display:flex;justify-content:center;align-items:center;gap:22px;font-size:13px}
.contact-strip .sep{color:#888}
.contact-strip span{display:flex;align-items:center;gap:9px}
.foot-line{left:100px;width:1000px;height:1px;background:var(--footer-line)}
.foot-col h5{font-size:12.5px;font-weight:600;color:#eee;text-transform:uppercase;letter-spacing:.2px}
.foot-col ul{list-style:none;margin-top:12px}
.foot-col li{font-size:11px;line-height:22.5px;color:#cfd0d2}
.foot-col li::before{content:"•";margin-right:6px;color:#aaa}
.foot-vline{top:104px;width:1px;height:120px;background:var(--footer-line)}
.form-grid{display:grid;grid-template-columns:163px 163px;gap:5px 5px;margin-top:13px}
.form-grid div{height:22px;background:#6d6e70;color:#e5e5e5;font-size:10px;padding:0 8px;line-height:22px}
.submit{margin-top:7px;width:52px;height:20px;background:var(--mint);color:var(--white);font-size:9px;line-height:20px;text-align:center}
.newsletter{display:flex;margin-top:13px}
.newsletter .field{width:125px;height:27px;background:var(--white);color:#999;font-size:10px;padding:0 8px;line-height:27px}
.newsletter .send{width:30px;height:27px;background:#c9cacc;display:flex;align-items:center;justify-content:center}
.foot-links{left:100px;top:256px;font-size:10px;color:#ddd}
.copyright{left:100px;top:277px;font-size:10px;color:#ddd}
.foot-social{left:855px;top:259px;display:flex;gap:6px}
.foot-social span{width:28px;height:28px;border-radius:50%;display:flex;align-items:center;justify-content:center;font-size:7px;color:var(--white);font-family:"Ubuntu",sans-serif}

/* Live chat tab */
.live-chat{position:absolute;left:1166px;top:703px;width:34px;height:122px;background:var(--ink-2);border-radius:3px 0 0 3px;color:var(--white);display:flex;flex-direction:column;align-items:center;justify-content:center;gap:8px}
.live-chat b{writing-mode:vertical-rl;transform:rotate(180deg);font-size:12px;font-weight:600;letter-spacing:1px}
</style>
</head>
<body>
<div class="page">

<header class="topbar">
  <div class="abs brand">
    <span class="brand-mark"></span>
    <span class="brand-name">Our Server<br>Lantern</span>
  </div>
  <div class="abs social-top"><span>Chatterly</span><span>Quipster</span><span>workRing</span><span>Orbitly+</span><span>Vidoplex</span></div>
  <div class="abs btn-top btn-login">
    <svg width="12" height="12" viewBox="0 0 12 12"><path d="M5 2h5v8H5M1 6h6M5 4l2 2-2 2" fill="none" stroke="#d8dce4" stroke-width="1.3"/></svg>Login</div>
  <div class="abs btn-top btn-register">
    <svg width="12" height="12" viewBox="0 0 12 12"><path d="M2 10l1-3 6-6 2 2-6 6z" fill="#d8dce4"/></svg>Register</div>
  <div class="abs search">Search
    <svg width="12" height="12" viewBox="0 0 12 12"><circle cx="5" cy="5" r="3.5" fill="none" stroke="#c9ced8" stroke-width="1.5"/><path d="M7.5 7.5l3 3" stroke="#c9ced8" stroke-width="1.6"/></svg></div>
</header>

<nav class="mainnav">
  <ul>
    <li class="active">Home</li>
    <li>About us</li>
    <li>Website hosting</li>
    <li>Dedicated server</li>
    <li>Domains</li>
    <li>Email solutions</li>
    <li>Support (Call - 470 118 2093)</li>
  </ul>
</nav>

<section class="hero">
  <div class="abs hero-visual" role="img" aria-label="Person touching a world map surrounded by domain extension tags"></div>
  <h1 class="abs hero-title">Pellentesque convallis<br>molestie enim</h1>
  <div class="abs domain-form">
    <div class="domain-input">www. your domain name</div>
    <div class="domain-select">.com
      <svg width="6" height="10" viewBox="0 0 6 10"><path d="M0 4l3-3 3 3M0 6l3 3 3-3" fill="none" stroke="#888"/></svg></div>
    <div class="domain-go"><svg width="14" height="14" viewBox="0 0 12 12"><circle cx="5" cy="5" r="3.5" fill="none" stroke="#fff" stroke-width="1.6"/><path d="M7.5 7.5l3 3" stroke="#fff" stroke-width="1.8"/></svg></div>
  </div>
  <svg class="abs hero-arrow" style="left:26px" width="14" height="26" viewBox="0 0 14 26"><path d="M12 2L2 13l10 11" fill="none" stroke="#8f959c" stroke-width="2"/></svg>
  <svg class="abs hero-arrow" style="left:1158px" width="14" height="26" viewBox="0 0 14 26"><path d="M2 2l10 11L2 24" fill="none" stroke="#8f959c" stroke-width="2"/></svg>
</section>

<section class="services">
  <div class="abs service current" style="left:92px">
    <div class="service-icon outline">
      <svg width="36" height="36" viewBox="0 0 36 36"><circle cx="18" cy="18" r="15" fill="var(--teal)"/><path d="M10 12c3-1 5 1 6 3s-1 4 1 6-1 5-3 5M22 8c-1 3 2 4 4 5s2 5 0 6" fill="none" stroke="#fff" stroke-width="2"/></svg>
    </div>
    <h3>Website Hosting</h3>
    <p>Aenean sed quam non sapien faucibus<br>consequat vitae sit amet orci.</p>
  </div>
  <div class="abs service" style="left:350px">
    <div class="service-icon">
      <svg width="34" height="38" viewBox="0 0 34 38"><ellipse cx="17" cy="6" rx="14" ry="5" fill="#fff"/><path d="M3 10c0 3 6 5 14 5s14-2 14-5v6c0 3-6 5-14 5S3 19 3 16zM3 20c0 3 6 5 14 5s14-2 14-5v6c0 3-6 5-14 5S3 29 3 26z" fill="#fff"/></svg>
    </div>
    <h3>Dedicated Server</h3>
    <p>Aenean sed quam non sapien faucibus<br>consequat vitae sit amet orci.</p>
  </div>
  <div class="abs service" style="left:610px">
    <div class="service-icon">
      <svg width="40" height="26" viewBox="0 0 40 26"><rect x="1" y="1" width="38" height="24" rx="3" fill="none" stroke="#fff" stroke-width="2"/><g fill="#fff"><rect x="6" y="6" width="4" height="3"/><rect x="12" y="6" width="4" height="3"/><rect x="18" y="6" width="4" height="3"/><rect x="24" y="6" width="4" height="3"/><rect x="30" y="6" width="4" height="3"/><rect x="6" y="12" width="4" height="3"/><rect x="12" y="12" width="4" height="3"/><rect x="18" y="12" width="4" height="3"/><rect x="24" y="12" width="4" height="3"/><rect x="30" y="12" width="4" height="3"/><rect x="10" y="18" width="20" height="3"/></g></svg>
    </div>
    <h3>Domain Name</h3>
    <p>Aenean sed quam non sapien faucibus<br>consequat vitae sit amet orci.</p>
  </div>
  <div class="abs service" style="left:868px">
    <div class="service-icon">
      <svg width="40" height="28" viewBox="0 0 40 28"><rect x="1" y="1" width="38" height="26" rx="2" fill="#fff"/><path d="M2 3l18 13L38 3" fill="none" stroke="#2aaea8" stroke-width="2.2"/></svg>
    </div>
    <h3>Email Solutions</h3>
    <p>Aenean sed quam non sapien faucibus<br>consequat vitae sit amet orci.</p>
  </div>
  <div class="abs divider"></div>
</section>

<section class="cases">
  <h2 class="abs section-title">Case Studies</h2>
  <div class="abs case case-1" role="img" aria-label="Video case study: dark data centre server racks">
    <span class="play"><svg width="12" height="14" viewBox="0 0 12 14"><path d="M1 1l10 6-10 6z" fill="#333"/></svg></span>
  </div>
  <div class="abs case case-2" role="img" aria-label="Video case study: technician working at a server rack">
    <span class="play teal"><svg width="12" height="14" viewBox="0 0 12 14"><path d="M1 1l10 6-10 6z" fill="#fff"/></svg></span>
  </div>
  <div class="abs case case-3" role="img" aria-label="Video case study: cloud network connecting devices">
    <span class="play"><svg width="12" height="14" viewBox="0 0 12 14"><path d="M1 1l10 6-10 6z" fill="#333"/></svg></span>
  </div>
  <div class="abs case-arrow" style="left:0"><svg width="8" height="12" viewBox="0 0 8 12"><path d="M6 1L1 6l5 5" fill="none" stroke="#fff" stroke-width="1.5"/></svg></div>
  <div class="abs case-arrow" style="left:1178px"><svg width="8" height="12" viewBox="0 0 8 12"><path d="M2 1l5 5-5 5" fill="none" stroke="#fff" stroke-width="1.5"/></svg></div>
</section>

<section class="testimonials">
  <h2 class="abs section-title">Testimonials</h2>
  <div class="abs quote-card">
    <div class="quote-photo" role="img" aria-label="Portrait of the customer"></div>
    <div class="quote-body">
      <div class="quote-name">Nate Corwin, <span>City</span>
        <svg width="86" height="14" viewBox="0 0 86 14"><g fill="var(--star)"><path id="st" d="M7 0l2 5h5l-4 3 1.6 5L7 10l-4.6 3L4 8 0 5h5z"/><use href="#st" x="17"/><use href="#st" x="34"/><use href="#st" x="51"/></g><path d="M75 0l2 5h5l-4 3 1.6 5L75 10z" fill="var(--star)"/><path d="M75 0l-2 5h-5l4 3-1.6 5L75 10z" fill="none" stroke="var(--star)"/></svg>
      </div>
      <p class="quote-text"><span class="qm" style="left:0;top:-4px">&ldquo;</span>Donec vestibulum odio sem, ac laoreet massa ullamcorper id. Donec nisi et tellus hendrerit vehicula. Nunc eu ligula sed quam pulvinar maximus in vitae eros. Proin porta fermentum , vel porttitor turpis venenatis luctus. Vivamus volutpat sapien quis tempus.<span class="qm" style="right:-30px;bottom:-34px">&rdquo;</span></p>
    </div>
  </div>
  <div class="abs dots"><i class="on"></i><i></i><i></i><i></i><i></i><i></i><i></i></div>
</section>

<section class="why">
  <h2 class="abs section-title">Why us?</h2>
  <p class="abs why-intro">Pellentesque blandit lacus eget nunc faucibus, et tincidunt eros viverra. Phasellus consequat sagittis nisl suscipit feugiat. Cras eget leo sed nunc hendrerit ultricies eu at nisl. Praesent iaculis faucibus urna sit amet lacinia. Maecenas consequat justo enim, ac mattis massa imperdiet quis. Fusce eget neque elit. Sed augue orci, elementum in magna congue, tincidunt vulputate erat. Aliquam consectetur orci molestie dictum molestie.</p>
  <div class="abs feature" style="left:134px">
    <h4><svg width="20" height="20" viewBox="0 0 20 20"><circle cx="10" cy="10" r="8" fill="none" stroke="#444" stroke-width="2"/><circle cx="10" cy="10" r="3.5" fill="none" stroke="#444" stroke-width="2"/><path d="M4 4l3.5 3.5M16 4l-3.5 3.5M4 16l3.5-3.5M16 16l-3.5-3.5" stroke="#444" stroke-width="2"/></svg>Best Support</h4>
    <p>Fusce vitae lectus sit amet mi pulvinar maximus. Aenean placerat, nibh vel accumsan aliquet, magna nibh accumsan.</p>
  </div>
  <div class="abs vline" style="left:428px"></div>
  <div class="abs feature" style="left:472px">
    <h4><svg width="20" height="14" viewBox="0 0 20 14"><rect x="1" y="1" width="18" height="12" fill="none" stroke="#444" stroke-width="2"/><circle cx="10" cy="7" r="3" fill="#444"/></svg>Affordable Price</h4>
    <p>Fusce vitae lectus sit amet mi pulvinar maximus. Aenean placerat, nibh vel accumsan aliquet, magna nibh accumsan.</p>
  </div>
  <div class="abs vline" style="left:770px"></div>
  <div class="abs feature" style="left:818px">
    <h4><svg width="16" height="20" viewBox="0 0 16 20"><path d="M1 1h9l5 5v13H1z" fill="none" stroke="#444" stroke-width="2"/><path d="M4 10h8M4 14h8" stroke="#444" stroke-width="1.5"/></svg>Best Domain Names</h4>
    <p>Fusce vitae lectus sit amet mi pulvinar maximus. Aenean placerat, nibh vel accumsan aliquet, magna nibh accumsan.</p>
  </div>
  <div class="abs why-line"></div>
  <div class="abs rating-label">We also have rating from our customers</div>
  <div class="abs rating-btn">
    <svg width="136" height="24" viewBox="0 0 136 24"><g fill="#fff"><path id="bs" d="M12 0l3.4 8H24l-7 5 2.7 9L12 17l-7.7 5L7 13 0 8h8.6z"/><use href="#bs" x="28"/><use href="#bs" x="56"/><use href="#bs" x="84"/></g><path d="M124 0l3.4 8h8.6l-7 5 2.7 9-7.7-5z" fill="#fff"/><path d="M124 0l-3.4 8H112l7 5-2.7 9 7.7-5" fill="none" stroke="#fff" stroke-width="1.5"/></svg>
    <span>(52 Reviews)</span>
  </div>
</section>

<section class="feed">
  <div class="abs feed-badge"><span style="width:22px;height:22px;border-radius:50%;background:#fff;display:block"></span></div>
  <div class="abs feed-handle">natecorwin@ourserverlantern</div>
  <div class="abs feed-text">Aenean sed quam non sapien faucibus consequat vitae sit amet orci sapien eu tellus finibus fermentum</div>
  <div class="abs feed-actions">
    <svg width="14" height="12" viewBox="0 0 14 12"><path d="M1 11c1-5 4-7 8-7V1l4 4-4 4V6c-3 0-6 1-8 5z" fill="#fff"/></svg>
    <svg width="14" height="12" viewBox="0 0 14 12"><path d="M1 3h3l5 6h4M1 9h3l5-6h4M11 1l2 2-2 2M11 7l2 2-2 2" fill="none" stroke="#fff" stroke-width="1.5"/></svg>
    <svg width="14" height="12" viewBox="0 0 14 12"><ellipse cx="7" cy="5" rx="6" ry="4.5" fill="#fff"/><path d="M3 8l-1 3 4-2z" fill="#fff"/></svg>
  </div>
</section>

<footer class="site-footer">
  <div class="abs contact-strip">
    <span><svg width="13" height="13" viewBox="0 0 13 13"><path d="M3 1l2 3-1.4 1.4a7 7 0 0 0 4 4L9 8l3 2-1.5 2.5C5 12 1 8 .5 2.5z" fill="#ddd"/></svg>Contact us today! 580 246 7715</span>
    <span class="sep">|</span>
    <span><svg width="14" height="10" viewBox="0 0 14 10"><rect width="14" height="10" fill="#ddd"/><path d="M0 0l7 5 7-5" fill="none" stroke="#333"/></svg>support@ourserverlantern.com</span>
    <span class="sep">|</span>
    <span><svg width="14" height="10" viewBox="0 0 14 10"><rect width="14" height="10" fill="#ddd"/><path d="M0 0l7 5 7-5" fill="none" stroke="#333"/></svg>info@ourserverlantern.com</span>
  </div>
  <div class="abs foot-line" style="top:76px"></div>

  <div class="abs foot-col" style="left:102px;top:101px">
    <h5>Contact us</h5>
    <div class="form-grid"><div>Name</div><div>Phone</div><div>E-mail</div><div>Message</div></div>
    <div class="submit">SUBMIT</div>
  </div>
  <div class="abs foot-vline" style="left:463px"></div>
  <div class="abs foot-col" style="left:488px;top:101px">
    <h5>Quick links</h5>
    <ul><li>Home</li><li>About us</li><li>Website Hosting</li><li>Dedicated Server</li></ul>
  </div>
  <div class="abs foot-vline" style="left:617px"></div>
  <div class="abs foot-col" style="left:641px;top:101px">
    <h5>More</h5>
    <ul><li>Domains</li><li>Email Solutions</li><li>Register</li><li>Login</li></ul>
  </div>
  <div class="abs foot-vline" style="left:770px"></div>
  <div class="abs foot-col" style="left:795px;top:101px">
    <h5>More</h5>
    <ul><li>FAQ</li><li>Support Center</li><li>Resources</li><li>Sitemap</li></ul>
  </div>
  <div class="abs foot-vline" style="left:914px"></div>
  <div class="abs foot-col" style="left:945px;top:101px">
    <h5>Newsletter</h5>
    <div class="newsletter"><div class="field">E-mail</div><div class="send"><svg width="10" height="12" viewBox="0 0 10 12"><path d="M1 1l8 5-8 5z" fill="#777"/></svg></div></div>
  </div>

  <div class="abs foot-line" style="top:239px"></div>
  <div class="abs foot-links">Home &nbsp;|&nbsp; Contact us &nbsp;|&nbsp; About us &nbsp;|&nbsp; Live Chat</div>
  <div class="abs copyright">Copyright &nbsp;© 2015 &nbsp;Our Server Lantern. &nbsp;All rights reserved.</div>
  <div class="abs foot-social">
    <span style="background:#3b5a98">Chat</span>
    <span style="background:#2aa9e0">Quip</span>
    <span style="background:#444">Orb+</span>
    <span style="background:#1a7bb9">work</span>
    <span style="background:#d33">Vido</span>
    <span style="border:2px solid #ddd"><svg width="12" height="9" viewBox="0 0 14 10"><rect width="14" height="10" fill="#ddd"/><path d="M0 0l7 5 7-5" fill="none" stroke="#333"/></svg></span>
    <span style="border:2px solid #aaa"><svg width="10" height="12" viewBox="0 0 10 12"><path d="M5 11V2M1 6l4-4 4 4" fill="none" stroke="#ccc" stroke-width="1.5"/></svg></span>
  </div>
</footer>

<aside class="live-chat">
  <b>LIVE CHAT</b>
  <svg width="14" height="12" viewBox="0 0 14 12"><ellipse cx="7" cy="5" rx="6" ry="4.5" fill="#fff"/><path d="M3 8l-1 3 4-2z" fill="#fff"/></svg>
</aside>

</div>
</body>
</html>
```